Ridgeway Builders, Inc. Concrete cutting special flyer , 10% off for new customers

Flyer to send to potential customers and business associates and general contractors - specializing in Concrete-Flatwork
Concrete Repair
Concrete Sidewalks
Patios & Driveways
Stoops, Porches And Staircase
Foundation Contractors--Concrete
Facade Restoration
Concrete
Patios
Driveways
Walkways
Commercial Concrete Work
Concrete Restoration
Building Alterations
Foundations - Concrete
Concrete Repairs
rbwxpo.com

Target Market(s)

Homeowners, business owners & general contractors

Industry/Entity Type

Construction

Font styles to use
Serif

Colors
FFC000
F8CF3A
FAE287
FDF2CF
FEFAEE
EB3D1F
EC4F4E
F09395
F8D3D4
FCEDEE

Requirements
Must have
• General Contracting, masonry - Must have Logo Please see list of services Ridgeway Builders NY, Inc., has to offer. Concrete-Flatwork Concrete Repair Concrete Sidewalks Patios & Driveways Stoops, Porches And Staircase Foundation Contractors--Concrete Facade Restoration Concrete Patios Driveways Walkways Commercial Concrete Work Concrete Restoration Building Alterations Foundations - Concrete Concrete Repairs
Nice to have
• List of services - Logo - Black & Gold with a bold color to stand out (preferably reds)

```html
<!DOCTYPE html>
<html lang="en">
<head>
<meta charset="utf-8">
<title>Ridgeway Builders NY, Inc. – Services Flyer</title>
<link rel="stylesheet" href="https://fonts.googleapis.com/css2?family=Montserrat:wght@600;700;800;900&family=Nunito:wght@500;600&display=swap">
<style>
:root{
  --red:#cd2027;
  --red-dark:#8e1519;
  --coral:#ec4f4e;
  --gold:#ffc000;
  --gold-soft:#f8cf3a;
  --ink:#231f20;
  --panel:#262626;
  --white:#ffffff;
  --green:#17402b;
}
*{margin:0;padding:0;box-sizing:border-box}
html,body{width:861px;height:1200px;overflow:hidden;background:var(--white)}
.flyer{position:relative;width:861px;height:1200px;overflow:hidden;font-family:"Montserrat",sans-serif}

/* left column */
.side{position:absolute;left:0;top:0;width:337px;height:1200px;background:var(--red)}
.side-top{position:absolute;left:0;top:0}
.brand{position:absolute;left:0;top:150px;width:337px;text-align:center;color:var(--green);font-weight:800;font-size:30px;line-height:34px;letter-spacing:.5px}
.brand-mark{display:block;width:22px;height:22px;background:var(--green);margin:0 auto 10px}

.services-title{position:absolute;left:26px;top:330px;color:var(--ink);font-weight:900;line-height:.95}
.services-title .l1{display:block;font-size:40px}
.services-title .l2{display:block;font-size:47px;letter-spacing:-.5px}

.service-list{position:absolute;left:26px;top:436px;list-style:none;width:300px}
.service-list li{position:relative;padding-left:22px;color:var(--white);font-weight:700;font-size:16px;line-height:21.5px;margin-bottom:4.7px}
.service-list li svg{position:absolute;left:0;top:5px;width:13px;height:13px}

.offer{position:absolute;left:26px;top:933px;width:287px;height:95px;border:2px dashed var(--white);padding:8px 0 0 10px}
.offer .pct{color:var(--gold-soft);font-weight:900;font-size:44px;line-height:44px}
.offer .off{color:var(--gold-soft);font-weight:800;font-size:27px;letter-spacing:1px}
.offer .new{display:block;color:var(--gold-soft);font-weight:800;font-size:22px;letter-spacing:2.5px;line-height:30px}

.call{position:absolute;left:27px;top:1036px;color:var(--white);font-weight:900;font-size:28px;letter-spacing:4.5px}
.phone-icon{position:absolute;left:26px;top:1088px;width:26px;height:42px}
.phones{position:absolute;left:65px;top:1070px;color:var(--white);font-weight:900;font-size:34px;line-height:36px;letter-spacing:-.5px}
.web{position:absolute;left:28px;top:1148px;color:var(--white);font-weight:600;font-size:18px;letter-spacing:10.6px}

/* right panel */
.panel{position:absolute;left:337px;top:0;width:516px;height:1200px;background:var(--panel)}
.headline{position:absolute;left:357px;top:42px;color:var(--coral);font-weight:900;line-height:1}
.headline .big{display:block;font-size:57px;letter-spacing:1px}
.headline .sub{display:block;font-size:31.5px;line-height:33px;letter-spacing:.3px;margin-top:4px}
.tagline{position:absolute;left:357px;top:210px;width:485px;text-align:center;color:var(--white);font-weight:800;font-size:20.5px;line-height:27px}
.machine{position:absolute;left:330px;top:276px;width:488px;height:390px;border-radius:6px;background:linear-gradient(160deg,#f2c230 0%,#e3ab18 45%,#3a3a3a 80%,#262626 100%)}

.rule{position:absolute;left:357px;width:478px;border-top:2px dotted var(--coral)}
.provide{position:absolute;left:362px;top:688px;font-weight:900;line-height:1}
.provide .a{display:block;color:var(--coral);font-size:32px}
.provide .b{display:block;color:var(--white);font-size:32px;margin-top:4px}
.about{position:absolute;left:361px;top:766px;width:480px;color:var(--white);font-family:"Nunito",sans-serif;font-weight:600;font-size:15.8px;line-height:21px}
.why{position:absolute;left:355px;color:var(--white);font-weight:900;font-size:24.5px}
.why-text{position:absolute;left:355px;width:473px;color:var(--coral);font-weight:600;font-size:14.3px;line-height:19px;text-align:justify;text-align-last:left}

.hazard{position:absolute;left:337px;top:1184px;width:516px;height:16px;background:repeating-linear-gradient(135deg,var(--gold) 0 14px,var(--ink) 14px 28px)}
</style>
</head>
<body>
<div class="flyer">

  <aside class="side">
    <svg class="side-top" width="337" height="320" viewBox="0 0 337 320" aria-hidden="true">
      <polygon points="0,0 337,0 337,252 111,318 0,268" fill="var(--red-dark)"/>
      <polygon points="0,0 337,0 337,233 111,301 0,251" fill="var(--white)"/>
    </svg>
    <div class="brand"><span class="brand-mark"></span>Ridgeway Builders<br>NY, Inc.</div>

    <h2 class="services-title"><span class="l1">OUR</span><span class="l2">SERVICES</span></h2>

    <ul class="service-list">
      <li><svg viewBox="0 0 14 14"><circle cx="7" cy="7" r="7" fill="var(--gold)"/><path d="M3.8 7.2l2.2 2.2 4.2-4.4" fill="none" stroke="var(--red)" stroke-width="1.8"/></svg>FLATWORK</li>
      <li><svg viewBox="0 0 14 14"><circle cx="7" cy="7" r="7" fill="var(--gold)"/><path d="M3.8 7.2l2.2 2.2 4.2-4.4" fill="none" stroke="var(--red)" stroke-width="1.8"/></svg>CONCRETE REPAIR</li>
      <li><svg viewBox="0 0 14 14"><circle cx="7" cy="7" r="7" fill="var(--gold)"/><path d="M3.8 7.2l2.2 2.2 4.2-4.4" fill="none" stroke="var(--red)" stroke-width="1.8"/></svg>CONCRETE SIDEWALKS</li>
      <li><svg viewBox="0 0 14 14"><circle cx="7" cy="7" r="7" fill="var(--gold)"/><path d="M3.8 7.2l2.2 2.2 4.2-4.4" fill="none" stroke="var(--red)" stroke-width="1.8"/></svg>PATIOS &amp; DRIVEWAYS</li>
      <li><svg viewBox="0 0 14 14"><circle cx="7" cy="7" r="7" fill="var(--gold)"/><path d="M3.8 7.2l2.2 2.2 4.2-4.4" fill="none" stroke="var(--red)" stroke-width="1.8"/></svg>STOOPS, PORCHES AND</li>
      <li><svg viewBox="0 0 14 14"><circle cx="7" cy="7" r="7" fill="var(--gold)"/><path d="M3.8 7.2l2.2 2.2 4.2-4.4" fill="none" stroke="var(--red)" stroke-width="1.8"/></svg>STAIRCASE</li>
      <li><svg viewBox="0 0 14 14"><circle cx="7" cy="7" r="7" fill="var(--gold)"/><path d="M3.8 7.2l2.2 2.2 4.2-4.4" fill="none" stroke="var(--red)" stroke-width="1.8"/></svg>FOUNDATION CONTRACTORS CONCRETE</li>
      <li><svg viewBox="0 0 14 14"><circle cx="7" cy="7" r="7" fill="var(--gold)"/><path d="M3.8 7.2l2.2 2.2 4.2-4.4" fill="none" stroke="var(--red)" stroke-width="1.8"/></svg>FACADE RESTORATION</li>
      <li><svg viewBox="0 0 14 14"><circle cx="7" cy="7" r="7" fill="var(--gold)"/><path d="M3.8 7.2l2.2 2.2 4.2-4.4" fill="none" stroke="var(--red)" stroke-width="1.8"/></svg>CONCRETE</li>
      <li><svg viewBox="0 0 14 14"><circle cx="7" cy="7" r="7" fill="var(--gold)"/><path d="M3.8 7.2l2.2 2.2 4.2-4.4" fill="none" stroke="var(--red)" stroke-width="1.8"/></svg>PATIOS</li>
      <li><svg viewBox="0 0 14 14"><circle cx="7" cy="7" r="7" fill="var(--gold)"/><path d="M3.8 7.2l2.2 2.2 4.2-4.4" fill="none" stroke="var(--red)" stroke-width="1.8"/></svg>DRIVEWAYS</li>
      <li><svg viewBox="0 0 14 14"><circle cx="7" cy="7" r="7" fill="var(--gold)"/><path d="M3.8 7.2l2.2 2.2 4.2-4.4" fill="none" stroke="var(--red)" stroke-width="1.8"/></svg>WALKWAYS</li>
      <li><svg viewBox="0 0 14 14"><circle cx="7" cy="7" r="7" fill="var(--gold)"/><path d="M3.8 7.2l2.2 2.2 4.2-4.4" fill="none" stroke="var(--red)" stroke-width="1.8"/></svg>COMMERCIAL CONCRETE WORK</li>
      <li><svg viewBox="0 0 14 14"><circle cx="7" cy="7" r="7" fill="var(--gold)"/><path d="M3.8 7.2l2.2 2.2 4.2-4.4" fill="none" stroke="var(--red)" stroke-width="1.8"/></svg>CONCRETE RESTORATION</li>
      <li><svg viewBox="0 0 14 14"><circle cx="7" cy="7" r="7" fill="var(--gold)"/><path d="M3.8 7.2l2.2 2.2 4.2-4.4" fill="none" stroke="var(--red)" stroke-width="1.8"/></svg>BUILDING ALTERATIONS</li>
      <li><svg viewBox="0 0 14 14"><circle cx="7" cy="7" r="7" fill="var(--gold)"/><path d="M3.8 7.2l2.2 2.2 4.2-4.4" fill="none" stroke="var(--red)" stroke-width="1.8"/></svg>FOUNDATIONS - CONCRETE</li>
      <li><svg viewBox="0 0 14 14"><circle cx="7" cy="7" r="7" fill="var(--gold)"/><path d="M3.8 7.2l2.2 2.2 4.2-4.4" fill="none" stroke="var(--red)" stroke-width="1.8"/></svg>CONCRETE REPAIRS</li>
    </ul>

    <div class="offer">
      <span class="pct">10%</span> <span class="off">OFF FOR</span>
      <span class="new">NEW CUSTOMERS</span>
    </div>

    <div class="call">CALL US NOW!</div>
    <svg class="phone-icon" viewBox="0 0 26 42" aria-hidden="true">
      <rect x="2" y="2" width="22" height="38" rx="4" fill="none" stroke="var(--white)" stroke-width="3"/>
      <rect x="9" y="33" width="8" height="3" rx="1.5" fill="var(--white)"/>
    </svg>
    <div class="phones">555-201-4830<br>555-201-7761</div>
    <div class="web">www.rbwxpo.com</div>
  </aside>

  <main class="panel"></main>

  <h1 class="headline">
    <span class="big">NY'S LEADING</span>
    <span class="sub">EXCAVATION,FOUNDTION,</span>
    <span class="sub">WATERPROOFING AND</span>
    <span class="sub">FLAT ROOF SPECIALISTS</span>
  </h1>
  <p class="tagline">WE'LL GET THE JOB DONE RITE<br>THE FIRST TIME!!</p>

  <div class="machine" role="img" aria-label="Yellow tracked excavator with raised boom and bucket"></div>

  <div class="rule" style="top:677px"></div>
  <h2 class="provide"><span class="a">WE PROVIDE</span><span class="b">THE BEST SERVICES</span></h2>
  <p class="about">Our projects include both Residential and Commercial construction and repairs/restorations. Occupied and fully operational job sites are never a problem. And we can also plan, manage, and build multi-phase jobs. we specialize in excavation, foundation, Roofing and waterproofing.</p>

  <div class="rule" style="top:886px"></div>
  <h3 class="why" style="top:897px">WHY CHOOSE US?</h3>
  <p class="why-text" style="top:934px">WE OFFER AN END-TO-END CLIENT EXPERIENCE THAT INCLUDES SEAMLESS COMMUNICATION, BUDGETING, STAFFING,ON-SITE ORGANIZATION, AND SOLID, QUALITY HANDIWORK EVERY TIME.</p>

  <div class="rule" style="top:1027px"></div>
  <h3 class="why" style="top:1038px">WHY CHOOSE US?</h3>
  <p class="why-text" style="top:1074px">WE WORK WITH ARCHITECTS AND DESIGNERS TO PRODUCE BEAUTIFUL, FUNCTIONAL STRUCTURES. CALL US TODAY AND BRING OUR PROJECT MANAGEMENT SKILLS AND EXTENSIVE CONSTRUCTION EXPERIENCE TO YOUR NEXT PROJECT.</p>

  <div class="hazard"></div>
</div>
</body>
</html>
```